Home loan promotion flyer (DL or Postcard)

We need a flyer that promotes our home loan broking service. In summary, we are an Australian financial planning business that helps Gen X and Y make better financial planning decisions.

We would like the design to have a similar look and feel to the following:
http://www.leaflet-vault.com.au/qmpr/bright_path_steady_living/

Text that I would like included is:

(HEADING) Awesome Debt Management: Someone else's money used to Your advantage.

(Paragraph) Debt is not necessarily a dirty work. Smart Australian investors often use debt strategies to minimise tax burdens, pay off their home loan sooner and to build their wealth quicker.

(Promotion) Bring this along to your COMPLIMENTARY finance health check and we will give you a $25 Durban Vale voucher to celebrate your first step towards a better financial future. (Please include the image of the voucher near this text).

Finally, you must include our number (1300 614 972) and website (www.qmpr.com.au)

Apart from being consistent with the e-brochure above (please ensure you view the link), we would like the design to be bold and stand out from the crowd.

I have attached a previous home loan promotion design that I like but I feel that there are too many words and not enough space. Please use the good elements but avoid the rest.

Finally, I've also attached a DL "goldfish" design that I really like because I think the design is memorable and stands-out.
Updates

Reason: Hi there designers Thanks for your designs so far. They look great. I have extended the brief to give everyone the opportunity to reassess their design to make sure that it is consistent with the design brief. If anything is unclear please don't hesitate to make contact. Thanks TR

Target Market(s)

Australian first home buyers and property investors.

Industry/Entity Type

Financial

Requirements
Must have
• The design MUST be consistent with the existing marketing material referred to in this link.

```html
<!DOCTYPE html>
<html lang="en">
<head>
<meta charset="utf-8">
<title>Awesome Debt Management – Flyer</title>
<link rel="stylesheet" href="https://fonts.googleapis.com/css2?family=Didact+Gothic&display=swap">
<style>
  :root {
    --navy: #1d2b57;
    --ink: #2a3766;
    --paper: #ffffff;
    --frame: #3a3a3a;
    --ribbon-light: #7fd3ec;
    --ribbon-mid: #2fb3dc;
    --ribbon-deep: #1590bd;
    --tag-edge: #5cc3e6;
    --tag-text: #1a1a1a;
    --card-dark: #1a1a1a;
    --card-silver: #c9c9c9;
    --brand-green: #8cc63f;
  }
  * { margin: 0; padding: 0; box-sizing: border-box; }
  html, body {
    width: 1200px;
    height: 1170px;
    overflow: hidden;
    background: var(--paper);
    font-family: "Didact Gothic", "Century Gothic", sans-serif;
  }
  .canvas {
    position: relative;
    width: 1200px;
    height: 1170px;
  }
  .panel {
    position: absolute;
    left: 49px;
    width: 1124px;
    height: 537px;
    border: 1.5px solid var(--frame);
    background: var(--paper);
    overflow: hidden;
  }
  .panel--front { top: 19px; }
  .panel--back { top: 632px; }

  .headline {
    position: absolute;
    left: 36px;
    top: 97px;
    color: var(--navy);
    font-size: 55px;
    line-height: 84px;
    font-weight: 400;
    letter-spacing: 0.3px;
    -webkit-text-stroke: 1.4px var(--navy);
  }

  .gift-photo {
    position: absolute;
    left: 517px;
    top: 42px;
    width: 607px;
    height: 495px;
    background:
      radial-gradient(ellipse at 45% 35%, var(--ribbon-light) 0%, var(--ribbon-mid) 40%, transparent 70%),
      linear-gradient(160deg, var(--ribbon-mid) 0%, var(--ribbon-deep) 100%);
    border-top-left-radius: 40px;
  }

  .gift-tag {
    position: absolute;
    left: 905px;
    top: 180px;
    width: 200px;
    height: 176px;
    background: var(--paper);
    border: 8px solid var(--tag-edge);
    transform: rotate(-12deg);
    display: flex;
    align-items: center;
    padding-left: 18px;
  }
  .gift-tag__title {
    color: var(--tag-text);
    font-size: 25px;
    line-height: 32px;
    font-weight: 400;
  }

  .intro {
    position: absolute;
    left: 53px;
    top: 42px;
    color: var(--ink);
  }
  .intro__title {
    font-size: 33px;
    line-height: 38px;
    font-weight: 400;
  }
  .intro__body {
    font-size: 23px;
    line-height: 34px;
    margin-top: 0;
  }
  .intro__offer {
    font-size: 23px;
    line-height: 34px;
    margin-top: 32px;
  }

  .voucher {
    position: absolute;
    left: 57px;
    top: 324px;
    width: 290px;
    height: 188px;
    border-radius: 10px;
    transform: rotate(-3deg);
    background:
      radial-gradient(ellipse at 45% 55%, var(--card-silver) 0%, #6d6d6d 30%, var(--card-dark) 60%);
    box-shadow: 0 1px 2px rgba(0,0,0,0.3);
  }

  .contact {
    position: absolute;
    right: 58px;
    top: 356px;
    color: var(--ink);
    font-size: 20px;
    line-height: 26px;
    text-align: right;
  }

  .brand {
    position: absolute;
    right: 58px;
    top: 410px;
    display: flex;
    align-items: center;
    gap: 12px;
  }
  .brand__mark {
    width: 56px;
    height: 70px;
    background: var(--brand-green);
  }
  .brand__name {
    font-size: 24px;
    line-height: 28px;
    color: var(--card-dark);
  }
</style>
</head>
<body>
<main class="canvas">
  <section class="panel panel--front">
    <h1 class="headline">Someone else's<br>money used to<br>Your advantage.</h1>
    <div class="gift-photo" role="img" aria-label="Photograph of a turquoise wrapped gift box with a satin bow"></div>
    <div class="gift-tag">
      <h2 class="gift-tag__title">Awesome<br>Debt<br>Management</h2>
    </div>
  </section>

  <section class="panel panel--back">
    <div class="intro">
      <h2 class="intro__title">Debt is not necessarily a dirty work.</h2>
      <p class="intro__body">Smart Australian investors often use debt strategies to minimise tax<br>burdens, pay off their home loan sooner and to build their wealth quicker.</p>
      <p class="intro__offer">Bring this along to your COMPLIMENTARY finance health check and<br>we will give you a $25 Durban Vale voucher to celebrate your first step<br>towards a better financial future.</p>
    </div>

    <div class="voucher" role="img" aria-label="Black gift card showing a silver wrapped present"></div>

    <p class="contact">1300 614 972 &nbsp;·&nbsp; www.qmpr.com.au</p>

    <div class="brand">
      <span class="brand__mark"></span>
      <span class="brand__name">Meridian<br>Wealth Planning</span>
    </div>
  </section>
</main>
</body>
</html>
```